Torretta Gelato Pints

6 flavors , pints italian , southern , organic , natural feel

Pistachio , chocolate, strawberry , hazelnut , vaniglia

Stracciiatelle

Target Market(s)

Upscale

Requirements
Must have
• See graphic upload . Want that look.. showing freshbest quality in gradients of each flavor

```html
<!DOCTYPE html>
<html lang="en">
<head>
<meta charset="utf-8">
<title>Torretta Gelato Pints — Strawberry Stracciatelle</title>
<link rel="stylesheet" href="https://fonts.googleapis.com/css2?family=Noto+Sans:wght@400;700&display=swap">
<style>
  :root {
    --backdrop: #e4e4e4;
    --label-red: #e3231f;
    --label-deep: #b80a0f;
    --label-light: #f26a55;
    --band-red: #c10d12;
    --ink-white: #f4f4f4;
    --ink-maroon: #6e0a0c;
    --ink-dark: #2a0606;
  }
  * { margin: 0; padding: 0; box-sizing: border-box; }
  html, body {
    width: 1200px;
    height: 960px;
    overflow: hidden;
    background: var(--backdrop);
    font-family: "Noto Sans", sans-serif;
  }
  .canvas {
    position: relative;
    width: 1200px;
    height: 960px;
    display: flex;
    align-items: center;
    justify-content: center;
  }
  .tub-label {
    position: relative;
    width: 820px;
    height: 680px;
    overflow: hidden;
  }
  .label-texture {
    position: absolute;
    inset: 0;
    background:
      radial-gradient(ellipse at 70% 75%, var(--label-light) 0%, rgba(242,106,85,0) 55%),
      linear-gradient(135deg, var(--label-deep) 0%, var(--label-red) 45%, var(--label-light) 100%);
  }
  .label-content {
    position: relative;
    height: 100%;
    display: flex;
    flex-direction: column;
    align-items: center;
    padding-top: 90px;
  }
  .brand-name {
    color: var(--ink-white);
    font-weight: 700;
    text-align: center;
    line-height: 1.05;
  }
  .brand-name .brand-main {
    display: block;
    font-size: 104px;
    letter-spacing: 1px;
  }
  .brand-name .brand-sub {
    display: block;
    font-size: 46px;
    margin-top: 6px;
  }
  .flavor-band {
    margin-top: 64px;
    width: 400px;
    height: 64px;
    background: var(--band-red);
    color: var(--ink-white);
    font-size: 42px;
    font-weight: 400;
    letter-spacing: 1px;
    display: flex;
    align-items: center;
    justify-content: center;
  }
  .flavor-variant {
    margin-top: 12px;
    color: var(--ink-maroon);
    font-size: 44px;
    font-weight: 400;
  }
  .product-notes {
    margin-top: 18px;
    color: var(--ink-dark);
    font-size: 22px;
    text-align: center;
    line-height: 1.35;
  }
</style>
</head>
<body>
  <main class="canvas">
    <section class="tub-label">
      <div class="label-texture" role="img" aria-label="Red strawberry-toned mosaic texture background"></div>
      <div class="label-content">
        <h1 class="brand-name">
          <span class="brand-main">Torretta</span>
          <span class="brand-sub">Gelato Pints</span>
        </h1>
        <p class="flavor-band">STRAWBERRY</p>
        <p class="flavor-variant">Stracciatelle</p>
        <p class="product-notes">Pints Italian , Southern , Organic<br>Natural Feel</p>
      </div>
    </section>
  </main>
</body>
</html>
```